Pulsewell Power sharing solutions, we offer different types of mobile charging stations for all ty

I need an app that shows all the locations that use our charging stations.
the app should show the following:

1. a map where client can see where all the stations are
2. a map that shows which one is the nearest charging station based on the persons location
3. a search tab where you can pick the city ( all will be based from sweden) and we will start with two cities: Gothenburg and Stockholm. So user will be able to pick the city and than get a list of all venues using our stations. along the way we will keep adding cities and countries but for now i need a design, something i can show potential customers on a power point how this app will work.
4. a list of different venue categories:
- restaurant
- café
- Festival
- Airport
- Library
- Night club
- Shopping center

Once client chooses the city, they can also choose what they are looking for and choose for example which restaurant to eat at based on if they have our charging station or not

you can of course improvise on ideas, if you come up with something and want to add to the app design thats ok, I'm up for suggestions.

in conclusion: the purpose for the app is for users to be able to search for charging stations or see where the nearest charging station is

Target Market(s)

Everyone

Requirements
Must have
• professional and simple design

```html
<!DOCTYPE html>
<html lang="en">
<head>
<meta charset="utf-8">
<title>Pulsewell Power – App Flow</title>
<link href="https://fonts.googleapis.com/css2?family=Poppins:wght@400;500&display=swap" rel="stylesheet">
<style>
:root{
  --bg:#0b0b0b;
  --bg-glow:#1e1a1a;
  --green:#3cb34a;
  --green-dark:#2e9a3c;
  --ink:#2a2f33;
  --label:#ffffff;
  --muted:#8d8d8d;
  --card:#fbf8f1;
  --strip:#ececec;
  --tray:#f4f4f4;
  --red:#e02a2a;
}
*{box-sizing:border-box;margin:0;padding:0}
html,body{width:1200px;height:1200px;overflow:hidden}
body{
  background:radial-gradient(ellipse at 25% 20%,var(--bg-glow),transparent 55%),
             radial-gradient(ellipse at 70% 75%,#1c1414,transparent 50%),var(--bg);
  font-family:"Poppins",sans-serif;position:relative;
}
.flow-label{position:absolute;color:var(--label);font-size:24px;font-weight:500;line-height:1.2;white-space:nowrap}
.connector{position:absolute;border-color:var(--label);border-style:solid;border-width:0}

.brand{position:absolute;left:70px;top:712px;width:200px;display:flex;align-items:center;gap:12px}
.brand-dot{width:44px;height:44px;border-radius:50%;background:var(--green);flex:none}
.brand-name{color:var(--green);font-size:24px;font-weight:500;line-height:1.1}

.phone{position:absolute;width:297px;height:526px;background:var(--tray);overflow:hidden}
.status{position:absolute;top:0;left:0;right:0;height:16px;display:flex;justify-content:space-between;align-items:center;padding:0 6px;font-size:6px;color:#333;z-index:3}
.search{position:absolute;top:23px;left:14px;width:269px;height:30px;border-radius:15px;background:var(--green);display:flex;align-items:center;padding:0 12px;color:#fff;font-size:11px;z-index:3}
.search-text{flex:1;margin-left:10px}
.search-divider{width:1px;height:30px;background:rgba(255,255,255,.35);margin-right:14px}
.map{position:absolute;top:0;left:0;width:297px;height:440px;display:block}
.strip{position:absolute;top:440px;left:0;right:0;height:18px;background:var(--strip);font-size:9px;color:#777;padding:3px 14px}
.tray{position:absolute;top:458px;left:0;right:0;height:68px;display:flex;gap:24px;padding:7px 0 0 10px}
.cat{width:40px;flex:none;text-align:center;font-size:7px;color:#aaa}
.cat-icon{width:40px;height:40px;border-radius:50%;border:1.5px solid #d0d0d0;background:#fff;display:flex;align-items:center;justify-content:center;margin-bottom:4px}
.cat.is-active .cat-icon{background:var(--green);border-color:var(--green-dark)}
.cat.is-active{color:var(--green)}

.card{position:absolute;left:6px;width:282px;background:var(--card);border-radius:4px;box-shadow:0 2px 8px rgba(0,0,0,.25);z-index:4}
.venue{position:relative;display:flex;padding:14px 12px 0 15px;gap:14px}
.venue::before{content:"";position:absolute;left:8px;top:12px;width:6px;height:6px;border-radius:50%;background:var(--green)}
.venue-photo{width:56px;height:56px;border-radius:50%;flex:none;background:radial-gradient(circle at 45% 55%,#6d7a3a,#3b4424 60%,#222 100%)}
.venue-name{font-size:11.5px;color:#222}
.venue-meta{font-size:9px;color:#8a8a8a;line-height:1.25}
.stars{color:var(--green);font-size:9px;letter-spacing:2px;margin-top:2px}
.nearest{font-size:9px;color:#8a8a8a;text-align:right;padding:8px 14px 8px 0}
.station{position:relative;display:flex;gap:14px;padding:12px 12px 10px 20px;border-top:1px dashed #bdbdbd}
.station::before{content:"";position:absolute;left:8px;top:12px;width:6px;height:6px;border-radius:50%;background:var(--green)}
.station-mark{width:34px;height:34px;border-radius:50%;background:var(--red);flex:none}
.station-name{font-size:9.5px;color:#222}
</style>
</head>
<body>

<svg width="0" height="0" style="position:absolute" aria-hidden="true">
  <defs>
    <symbol id="pin-station" viewBox="0 0 20 26">
      <path d="M10 1a9 9 0 0 0-9 9c0 6.5 9 15 9 15s9-8.5 9-15a9 9 0 0 0-9-9z" fill="#2a2f33" stroke="#fff" stroke-width="1.2"/>
      <circle cx="10" cy="10" r="5.5" fill="#fff"/>
      <circle cx="10" cy="10" r="3.2" fill="none" stroke="#3cb34a" stroke-width="1.6"/>
    </symbol>
    <symbol id="pin-venue" viewBox="0 0 20 26">
      <path d="M10 1a9 9 0 0 0-9 9c0 6.5 9 15 9 15s9-8.5 9-15a9 9 0 0 0-9-9z" fill="#3cb34a" stroke="#fff" stroke-width="1.2"/>
      <circle cx="10" cy="10" r="6" fill="#fff"/>
      <path d="M7.4 7.4l5.2 5.2M12.6 7.4l-5.2 5.2" stroke="#3cb34a" stroke-width="1.5" stroke-linecap="round"/>
    </symbol>
    <symbol id="you" viewBox="0 0 40 40">
      <circle cx="20" cy="20" r="20" fill="#7b6fd0" opacity=".22"/>
      <circle cx="20" cy="20" r="4" fill="#2f2fc8"/>
    </symbol>
    <symbol id="stations" viewBox="0 0 297 440">
      <use href="#you" x="37" y="249" width="40" height="40"/>
      <use href="#pin-station" x="95" y="70" width="18" height="24"/>
      <use href="#pin-station" x="38" y="122" width="18" height="24"/>
      <use href="#pin-station" x="67" y="136" width="18" height="24"/>
      <use href="#pin-station" x="5" y="151" width="18" height="24"/>
      <use href="#pin-station" x="169" y="140" width="18" height="24"/>
      <use href="#pin-station" x="215" y="217" width="18" height="24"/>
      <use href="#pin-station" x="264" y="228" width="18" height="24"/>
      <use href="#pin-station" x="249" y="244" width="18" height="24"/>
      <use href="#pin-station" x="79" y="328" width="18" height="24"/>
      <use href="#pin-station" x="147" y="328" width="18" height="24"/>
      <use href="#pin-station" x="208" y="328" width="18" height="24"/>
      <use href="#pin-station" x="133" y="372" width="18" height="24"/>
      <use href="#pin-station" x="93" y="381" width="18" height="24"/>
      <use href="#pin-station" x="207" y="394" width="18" height="24"/>
    </symbol>
    <symbol id="venues" viewBox="0 0 297 440">
      <use href="#pin-venue" x="78" y="110" width="18" height="24"/>
      <use href="#pin-venue" x="37" y="132" width="18" height="24"/>
      <use href="#pin-venue" x="21" y="174" width="18" height="24"/>
      <use href="#pin-venue" x="45" y="169" width="18" height="24"/>
      <use href="#pin-venue" x="69" y="177" width="18" height="24"/>
      <use href="#pin-venue" x="40" y="198" width="18" height="24"/>
      <use href="#pin-venue" x="128" y="184" width="18" height="24"/>
      <use href="#pin-venue" x="215" y="164" width="18" height="24"/>
      <use href="#pin-venue" x="148" y="241" width="18" height="24"/>
      <use href="#pin-venue" x="98" y="289" width="18" height="24"/>
      <use href="#pin-venue" x="5" y="300" width="18" height="24"/>
      <use href="#pin-venue" x="-2" y="347" width="18" height="24"/>
      <use href="#pin-venue" x="121" y="325" width="18" height="24"/>
      <use href="#pin-venue" x="169" y="352" width="18" height="24"/>
      <use href="#pin-venue" x="170" y="378" width="18" height="24"/>
      <use href="#pin-venue" x="215" y="352" width="18" height="24"/>
      <use href="#pin-venue" x="248" y="304" width="18" height="24"/>
      <use href="#pin-venue" x="63" y="423" width="18" height="24"/>
    </symbol>
    <linearGradient id="map-tone" x1="0" y1="0" x2="1" y2="1">
      <stop offset="0" stop-color="#e6e4dc"/>
      <stop offset=".45" stop-color="#d6e6c8"/>
      <stop offset=".7" stop-color="#e3e1d8"/>
      <stop offset="1" stop-color="#c9dfbf"/>
    </linearGradient>
    <symbol id="icon-cafe" viewBox="0 0 20 20"><path d="M4 8h9v4a4 4 0 0 1-4 4H8a4 4 0 0 1-4-4zM13 9h2a2 2 0 0 1 0 4h-2" fill="none" stroke="#bbb" stroke-width="1.5"/></symbol>
    <symbol id="icon-cross" viewBox="0 0 20 20"><path d="M5 5l10 10M15 5L5 15" stroke="currentColor" stroke-width="2" stroke-linecap="round"/></symbol>
    <symbol id="icon-festival" viewBox="0 0 20 20"><path d="M10 3l2 5 5 .5-4 3.5 1.2 5L10 14.5 5.8 17 7 12 3 8.5 8 8z" fill="#bbb"/></symbol>
    <symbol id="icon-plane" viewBox="0 0 20 20"><path d="M10 2c.8 0 1.2.8 1.2 2v4l6 3.5v1.5l-6-1.8v4l1.8 1.3V18L10 17l-3 1v-1.5L8.8 15v-4l-6 1.8v-1.5l6-3.5V4c0-1.2.4-2 1.2-2z" fill="#bbb"/></symbol>
    <symbol id="icon-book" viewBox="0 0 20 20"><path d="M5 3h8l2 2v12H7l-2-2z" fill="#bbb"/></symbol>
  </defs>
</svg>

<!-- flow labels and connectors -->
<div class="flow-label" style="left:94px;top:189px">After select City</div>
<div class="connector" style="left:184px;top:236px;width:152px;height:52px;border-left-width:4px;border-bottom-width:4px"></div>

<div class="flow-label" style="left:62px;top:468px">Venue Category Open</div>
<div class="connector" style="left:184px;top:514px;width:152px;height:52px;border-left-width:4px;border-bottom-width:4px"></div>

<div class="flow-label" style="left:998px;top:468px">Select Category</div>
<div class="connector" style="left:990px;top:514px;width:146px;height:46px;border-right-width:4px;border-bottom-width:4px"></div>

<div class="flow-label" style="left:946px;top:726px">Nearesr Charge<br>Station Find</div>
<div class="connector" style="left:917px;top:800px;width:88px;height:168px;border-right-width:4px;border-bottom-width:4px"></div>

<div class="flow-label" style="left:16px;top:1054px">Venue Details open</div>
<div class="connector" style="left:211px;top:874px;width:86px;height:166px;border-left-width:4px;border-top-width:4px"></div>

<div class="brand">
  <span class="brand-dot"></span>
  <span class="brand-name">Pulsewell<br>Power</span>
</div>

<!-- screen 1: after city selected -->
<section class="phone" style="left:348px;top:74px">
  <div class="status"><span>●●○○○ NT</span><span>12:53 pm</span><span>31% ▭</span></div>
  <div class="search">
    <svg width="11" height="11" viewBox="0 0 12 12"><circle cx="5" cy="5" r="4" fill="none" stroke="#fff" stroke-width="1.4"/><path d="M8 8l3 3" stroke="#fff" stroke-width="1.4"/></svg>
    <span class="search-text">Gothenburg</span><span class="search-divider"></span>
    <svg width="18" height="12" viewBox="0 0 18 12"><path d="M0 1h18M0 6h14M0 11h18" stroke="#fff" stroke-width="1.5"/></svg>
  </div>
  <svg class="map" viewBox="0 0 297 440" role="img" aria-label="Street map of Gothenburg with charging station pins">
    <rect width="297" height="440" fill="url(#map-tone)"/>
    <use href="#stations" width="297" height="440"/>
  </svg>
  <div class="strip">Venue Categories</div>
  <div class="tray">
    <div class="cat"><div class="cat-icon"><svg width="20" height="20"><use href="#icon-cafe"/></svg></div>Cafe</div>
    <div class="cat"><div class="cat-icon" style="color:#bbb"><svg width="20" height="20"><use href="#icon-cross"/></svg></div>Restaurant</div>
    <div class="cat"><div class="cat-icon"><svg width="20" height="20"><use href="#icon-festival"/></svg></div>Festival</div>
    <div class="cat"><div class="cat-icon"><svg width="20" height="20"><use href="#icon-plane"/></svg></div>Airport</div>
    <div class="cat"><div class="cat-icon"><svg width="20" height="20"><use href="#icon-book"/></svg></div>Library</div>
  </div>
</section>

<!-- screen 2: category selected -->
<section class="phone" style="left:681px;top:74px">
  <div class="status"><span>●●○○○ NT</span><span>12:53 pm</span><span>31% ▭</span></div>
  <div class="search">
    <svg width="11" height="11" viewBox="0 0 12 12"><circle cx="5" cy="5" r="4" fill="none" stroke="#fff" stroke-width="1.4"/><path d="M8 8l3 3" stroke="#fff" stroke-width="1.4"/></svg>
    <span class="search-text">Gothenburg</span><span class="search-divider"></span>
    <svg width="18" height="12" viewBox="0 0 18 12"><path d="M0 1h18M0 6h14M0 11h18" stroke="#fff" stroke-width="1.5"/></svg>
  </div>
  <svg class="map" viewBox="0 0 297 440" role="img" aria-label="Street map of Gothenburg with charging stations and restaurant pins">
    <rect width="297" height="440" fill="url(#map-tone)"/>
    <use href="#stations" width="297" height="440"/>
    <use href="#venues" width="297" height="440"/>
  </svg>
  <div class="strip">Venue Categories</div>
  <div class="tray">
    <div class="cat"><div class="cat-icon"><svg width="20" height="20"><use href="#icon-cafe"/></svg></div>Cafe</div>
    <div class="cat is-active"><div class="cat-icon" style="color:#fff"><svg width="20" height="20"><use href="#icon-cross"/></svg></div>Restaurant</div>
    <div class="cat"><div class="cat-icon"><svg width="20" height="20"><use href="#icon-festival"/></svg></div>Festival</div>
    <div class="cat"><div class="cat-icon"><svg width="20" height="20"><use href="#icon-plane"/></svg></div>Airport</div>
    <div class="cat"><div class="cat-icon"><svg width="20" height="20"><use href="#icon-book"/></svg></div>Library</div>
  </div>
</section>

<!-- screen 3: venue details -->
<section class="phone" style="left:297px;top:626px">
  <div class="status"><span>●●○○○ NT</span><span>12:53 pm</span><span>31% ▭</span></div>
  <div class="search">
    <svg width="11" height="11" viewBox="0 0 12 12"><circle cx="5" cy="5" r="4" fill="none" stroke="#fff" stroke-width="1.4"/><path d="M8 8l3 3" stroke="#fff" stroke-width="1.4"/></svg>
    <span class="search-text">Gothenburg</span><span class="search-divider"></span>
    <svg width="18" height="12" viewBox="0 0 18 12"><path d="M0 1h18M0 6h14M0 11h18" stroke="#fff" stroke-width="1.5"/></svg>
  </div>
  <svg class="map" viewBox="0 0 297 440" role="img" aria-label="Street map of Gothenburg with charging stations and restaurant pins">
    <rect width="297" height="440" fill="url(#map-tone)"/>
    <use href="#stations" width="297" height="440"/>
    <use href="#venues" width="297" height="440"/>
  </svg>
  <div class="card" style="top:177px">
    <div class="venue">
      <div class="venue-photo" role="img" aria-label="Photo of a dish served at the restaurant"></div>
      <div>
        <div class="venue-name">Lindqvist Kök</div>
        <div class="venue-meta">Verkstadsgatan 7, Gothenburg<br>411 40, Sweden<br>+46 31 55 01 23</div>
        <div class="stars">★★★★★</div>
      </div>
    </div>
    <div class="nearest">Nearest Chageing Station &nbsp;ϟ</div>
  </div>
  <div class="strip">Venue Categories</div>
  <div class="tray">
    <div class="cat"><div class="cat-icon"><svg width="20" height="20"><use href="#icon-cafe"/></svg></div>Cafe</div>
    <div class="cat is-active"><div class="cat-icon" style="color:#fff"><svg width="20" height="20"><use href="#icon-cross"/></svg></div>Restaurant</div>
    <div class="cat"><div class="cat-icon"><svg width="20" height="20"><use href="#icon-festival"/></svg></div>Festival</div>
    <div class="cat"><div class="cat-icon"><svg width="20" height="20"><use href="#icon-plane"/></svg></div>Airport</div>
    <div class="cat"><div class="cat-icon"><svg width="20" height="20"><use href="#icon-book"/></svg></div>Library</div>
  </div>
</section>

<!-- screen 4: nearest charging station -->
<section class="phone" style="left:613px;top:626px">
  <div class="status"><span>●●○○○ NT</span><span>12:53 pm</span><span>31% ▭</span></div>
  <div class="search">
    <svg width="11" height="11" viewBox="0 0 12 12"><circle cx="5" cy="5" r="4" fill="none" stroke="#fff" stroke-width="1.4"/><path d="M8 8l3 3" stroke="#fff" stroke-width="1.4"/></svg>
    <span class="search-text">Gothenburg</span><span class="search-divider"></span>
    <svg width="18" height="12" viewBox="0 0 18 12"><path d="M0 1h18M0 6h14M0 11h18" stroke="#fff" stroke-width="1.5"/></svg>
  </div>
  <svg class="map" viewBox="0 0 297 440" role="img" aria-label="Street map of Gothenburg with charging stations and restaurant pins">
    <rect width="297" height="440" fill="url(#map-tone)"/>
    <use href="#stations" width="297" height="440"/>
    <use href="#venues" width="297" height="440"/>
  </svg>
  <div class="card" style="top:180px">
    <div class="venue">
      <div class="venue-photo" role="img" aria-label="Photo of a dish served at the restaurant"></div>
      <div>
        <div class="venue-name">Lindqvist Kök</div>
        <div class="venue-meta">Verkstadsgatan 7, Gothenburg<br>411 40, Sweden<br>+46 31 55 01 23</div>
        <div class="stars">★★★★★</div>
      </div>
    </div>
    <div class="nearest">Nearest Chageing Station &nbsp;ϟ</div>
    <div class="station">
      <div class="station-mark"></div>
      <div>
        <div class="station-name">Voltara Car Charging Stations</div>
        <div class="venue-meta">Norra Smedjegatan 12, HÄLLNÄS</div>
        <div class="stars">★★★★</div>
        <div style="text-align:right;font-size:14px;color:#444;margin-top:-2px">ϟ</div>
      </div>
    </div>
  </div>
  <div class="strip">Venue Categories</div>
  <div class="tray">
    <div class="cat"><div class="cat-icon"><svg width="20" height="20"><use href="#icon-cafe"/></svg></div>Cafe</div>
    <div class="cat is-active"><div class="cat-icon" style="color:#fff"><svg width="20" height="20"><use href="#icon-cross"/></svg></div>Restaurant</div>
    <div class="cat"><div class="cat-icon"><svg width="20" height="20"><use href="#icon-festival"/></svg></div>Festival</div>
    <div class="cat"><div class="cat-icon"><svg width="20" height="20"><use href="#icon-plane"/></svg></div>Airport</div>
    <div class="cat"><div class="cat-icon"><svg width="20" height="20"><use href="#icon-book"/></svg></div>Library</div>
  </div>
</section>

</body>
</html>
```